Flyer-Design für Unternehmen der Alternativmedizin
Zielgruppe
Ich bin eine Einzelunternehmung im Bereich Alternativmedizin mit Akupunktur, Massagen, Craniosacral Therapie.
Aufgabenstellung
Titel: Individuelle Behandlung mit Alternativmedizin
Text schicke ich als Download.
Meine Farben sind die Komplementärfarben rot/grün.
Die Adresse muss mit drauf
Der Text darf anders formatiert werden. Auch rechtschreibefehler dürfen korrigiert werden.
Es darf auch ein Kartenausschnitt von z.B. Wegolo Karten benutzt werden.
Das Format sollte für einen Falzflyer von 105 x 210 mmDIN-Lang (Breite x Höhe in gefalztem Zustand) sein mit 2mm Beschnitt für die Druckerei. Oder anders gesagt 6-seitig, Din A4 mit Wickelfalz.
Ich liefere eigenes Bildmaterial, es darf aber auch etwas dazugenommen werden.

```html
<!DOCTYPE html>
<html lang="de">
<head>
<meta charset="utf-8">
<title>Faltflyer Praxis Lindhof</title>
<link rel="stylesheet" href="https://fonts.googleapis.com/css2?family=Montserrat:wght@500;600;700&family=Questrial&family=Roboto+Slab:wght@700&display=swap">
<style>
:root{
  --wine:#7a0a2c;
  --cream:#f8f8ec;
  --sage:#e6ecc4;
  --ink:#2b2b2b;
  --grey:#555;
  --accent-green:#8db33a;
  --stage:#d4d4d4;
}
*{box-sizing:border-box;margin:0;padding:0}
html,body{width:1200px;height:2400px;overflow:hidden;background:var(--stage)}
body{font-family:"Questrial",sans-serif;color:var(--ink);position:relative}
.spread{position:absolute;left:40px;width:1120px;height:792px;overflow:hidden;
  background:linear-gradient(135deg,var(--sage),var(--cream) 45%,var(--sage));
  box-shadow:0 18px 40px rgba(0,0,0,.18)}
.spread--inside{top:300px}
.spread--outside{top:1300px}
.shapes{position:absolute;inset:0;width:1120px;height:792px}
.photo{position:absolute;border-radius:50%;overflow:hidden}
.photo--rect{border-radius:0}
.badge{position:absolute;border-radius:50%;background:var(--wine);color:#fff;
  font-family:"Roboto Slab",serif;font-weight:700;text-align:center;
  display:flex;flex-direction:column;justify-content:center;align-items:center;line-height:1.15}
.badge::after{content:"";width:34px;height:1px;background:#fff;margin-top:6px}
.dot{position:absolute;border-radius:50%;background:var(--wine)}
.block{position:absolute}
.heading{font-family:"Montserrat",sans-serif;font-weight:600;color:var(--wine);
  font-size:19px;letter-spacing:.3px;text-transform:uppercase;padding-bottom:5px;
  border-bottom:2px solid var(--ink);display:inline-block;line-height:1.2}
.body-text{font-size:12px;line-height:1.45;color:var(--grey);margin-top:10px}
.label{font-family:"Montserrat",sans-serif;font-weight:700;font-size:10.5px;color:var(--ink);
  text-transform:uppercase;margin-top:10px;line-height:1.35}
.ticks{list-style:none;margin-top:8px}
.ticks li{font-size:11px;text-transform:uppercase;color:var(--grey);line-height:1.9;
  display:flex;align-items:center;gap:7px}
.ticks li svg{flex:none}
.quote{position:absolute;color:#fff;font-family:"Montserrat",sans-serif;font-weight:700;
  font-size:13.5px;line-height:1.35;text-align:center}
.quote-mark{font-family:"Roboto Slab",serif;font-size:46px;color:rgba(255,255,255,.35);position:absolute;line-height:1}
.panel-dark{color:#fff}
.panel-dark .heading{color:#fff;border-color:#fff}
.map{position:absolute;border:2px solid #fff;background:linear-gradient(135deg,#8a2141,#6f0927)}
.contact-line{font-size:13px;display:flex;align-items:center;gap:8px;line-height:1.7}
.web{font-family:"Montserrat",sans-serif;font-weight:600;font-size:16px;letter-spacing:.5px;
  padding-bottom:4px;border-bottom:2px solid #fff;display:inline-block}
.service{position:absolute;font-size:11px;color:var(--grey);line-height:1.3;white-space:nowrap}
.service::after{content:"";display:block;width:60px;height:2px;background:var(--accent-green);margin-top:5px}
.brand{position:absolute;right:28px;display:flex;align-items:center;gap:8px;font-family:"Montserrat",sans-serif;
  font-weight:600;font-size:20px;color:var(--wine)}
.brand-sub{position:absolute;right:28px;font-family:"Montserrat",sans-serif;font-weight:600;font-size:9px;
  color:var(--wine);letter-spacing:.4px;text-transform:uppercase;white-space:nowrap}
.brand-mark{width:12px;height:12px;border-radius:50%;background:var(--wine)}
.strong-note{font-family:"Montserrat",sans-serif;font-weight:700;font-size:11px;color:var(--wine);
  text-transform:uppercase;line-height:1.4}
.personal-quote{font-size:12.5px;color:var(--grey);line-height:1.45;font-style:italic;margin-top:10px}
</style>
</head>
<body>

<section class="spread spread--inside" aria-label="Innenseiten">
  <svg class="shapes" viewBox="0 0 1120 792" aria-hidden="true">
    <path d="M0 0H380V150Q250 215 0 232Z" fill="var(--wine)"/>
    <path d="M0 246Q230 232 380 168" fill="none" stroke="#111" stroke-width="6"/>
    <path d="M0 760Q420 730 760 650Q930 590 1120 470V792H0Z" fill="var(--wine)"/>
  </svg>

  <span class="quote-mark" style="left:18px;top:14px">“</span>
  <p class="quote" style="left:40px;top:34px;width:270px">Der Behandler hat eine Aufgabe: zu heilen.<br><br>Und wenn es ihm gelingt, ist es gleichgültig, auf welchem Wege es ihm gelingt.</p>
  <span class="quote-mark" style="left:300px;top:120px">”</span>

  <div class="photo" role="img" aria-label="Foto: Akupunkturbehandlung am Rücken, Kopfmassage im Hintergrund" style="left:360px;top:16px;width:320px;height:320px;background:radial-gradient(circle at 40% 55%,#f3c6a5,#e3a886 55%,#f4ece6)"></div>
  <div class="dot" style="left:735px;top:222px;width:22px;height:22px"></div>
  <div class="badge" style="left:640px;top:236px;width:108px;height:108px;font-size:13px">Ihre<br>Gesundheit<br>in guten<br>Händen</div>

  <div class="block" style="left:34px;top:270px;width:320px">
    <h2 class="heading">Chinesische Medizin (TCM)</h2>
    <p class="body-text">Die Traditionelle Chinesische Medizin (TCM) basiert auf über 2500 Jahre Erfahrung. Die Methoden die ich in meiner Praxis anwende sind Akupunktur, Heilkräuter, Schröpfen und Moxa. Mit TCM können diverse Symptombilder gelindert oder ganz zum Verschwinden gebracht werden.</p>
    <ul class="ticks">
      <li><svg width="11" height="11" viewBox="0 0 12 12"><circle cx="6" cy="6" r="6" fill="var(--wine)"/><path d="M3 6.2l2 2 4-4.4" stroke="#fff" stroke-width="1.6" fill="none"/></svg>Kopfschmerzen</li>
      <li><svg width="11" height="11" viewBox="0 0 12 12"><circle cx="6" cy="6" r="6" fill="var(--wine)"/><path d="M3 6.2l2 2 4-4.4" stroke="#fff" stroke-width="1.6" fill="none"/></svg>Verdauungsbeschwerden</li>
      <li><svg width="11" height="11" viewBox="0 0 12 12"><circle cx="6" cy="6" r="6" fill="var(--wine)"/><path d="M3 6.2l2 2 4-4.4" stroke="#fff" stroke-width="1.6" fill="none"/></svg>Heuschnupfen</li>
      <li><svg width="11" height="11" viewBox="0 0 12 12"><circle cx="6" cy="6" r="6" fill="var(--wine)"/><path d="M3 6.2l2 2 4-4.4" stroke="#fff" stroke-width="1.6" fill="none"/></svg>Gynäkologische Beschwerden</li>
      <li><svg width="11" height="11" viewBox="0 0 12 12"><circle cx="6" cy="6" r="6" fill="var(--wine)"/><path d="M3 6.2l2 2 4-4.4" stroke="#fff" stroke-width="1.6" fill="none"/></svg>Schlafstörungen</li>
      <li><svg width="11" height="11" viewBox="0 0 12 12"><circle cx="6" cy="6" r="6" fill="var(--wine)"/><path d="M3 6.2l2 2 4-4.4" stroke="#fff" stroke-width="1.6" fill="none"/></svg>Migräne</li>
      <li><svg width="11" height="11" viewBox="0 0 12 12"><circle cx="6" cy="6" r="6" fill="var(--wine)"/><path d="M3 6.2l2 2 4-4.4" stroke="#fff" stroke-width="1.6" fill="none"/></svg>Blasenentzündungen</li>
      <li><svg width="11" height="11" viewBox="0 0 12 12"><circle cx="6" cy="6" r="6" fill="var(--wine)"/><path d="M3 6.2l2 2 4-4.4" stroke="#fff" stroke-width="1.6" fill="none"/></svg>Gynäkologische Beschwerden</li>
      <li style="padding-left:18px">etc…</li>
    </ul>
  </div>

  <div class="block" style="left:400px;top:360px;width:300px">
    <h2 class="heading">Craniosacral Therapie</h2>
    <p class="body-text">Craniosacral Therapie ist ein Teilgebiet der Osteopathie und weit mehr als eine blosse Entspannungsmethode. Es wird das Gewebe gelöst und die Energien zum Fliessen gebracht. Dies alles mit sehr feinen Techniken.</p>
    <p class="label">Mögliche Anwendungsgebiete sind:</p>
    <ul class="ticks">
      <li><svg width="11" height="11" viewBox="0 0 12 12"><circle cx="6" cy="6" r="6" fill="var(--wine)"/><path d="M3 6.2l2 2 4-4.4" stroke="#fff" stroke-width="1.6" fill="none"/></svg>Prüfungsangst</li>
      <li><svg width="11" height="11" viewBox="0 0 12 12"><circle cx="6" cy="6" r="6" fill="var(--wine)"/><path d="M3 6.2l2 2 4-4.4" stroke="#fff" stroke-width="1.6" fill="none"/></svg>Schockzuständen</li>
      <li><svg width="11" height="11" viewBox="0 0 12 12"><circle cx="6" cy="6" r="6" fill="var(--wine)"/><path d="M3 6.2l2 2 4-4.4" stroke="#fff" stroke-width="1.6" fill="none"/></svg>Nacken- und Rückenschmerzen</li>
      <li><svg width="11" height="11" viewBox="0 0 12 12"><circle cx="6" cy="6" r="6" fill="var(--wine)"/><path d="M3 6.2l2 2 4-4.4" stroke="#fff" stroke-width="1.6" fill="none"/></svg>Schleudertraumas</li>
    </ul>
  </div>

  <div class="photo" role="img" aria-label="Foto: Schröpfgläser auf dem Rücken" style="left:340px;top:636px;width:150px;height:150px;background:radial-gradient(circle at 50% 45%,#f1e4d6,#d9b08e)"></div>
  <div class="photo" role="img" aria-label="Foto: Gesichtsbehandlung mit sanften Händen" style="left:478px;top:646px;width:136px;height:136px;background:radial-gradient(circle at 50% 50%,#f2cdb3,#c98c6f)"></div>

  <div class="block" style="left:782px;top:34px;width:310px">
    <h2 class="heading">Funktionelle Orthonomie<br>und Integration (FOI)</h2>
    <p class="body-text">Diese Therapiemethode wende ich für den Bewegungsapparat wie Rückenschmerzen, Knieschmerzen, Schulterbeschwerden etc. an. Sanft werden die Gelenke gelöst damit sie wieder Bewegungsfreiheit geniessen können.</p>
    <p class="label">Weitere Methoden, die ich häufig in meiner Praxis anwende sind:</p>
    <ul class="ticks">
      <li><svg width="11" height="11" viewBox="0 0 12 12"><circle cx="6" cy="6" r="6" fill="var(--wine)"/><path d="M3 6.2l2 2 4-4.4" stroke="#fff" stroke-width="1.6" fill="none"/></svg>Klassische Massage</li>
      <li><svg width="11" height="11" viewBox="0 0 12 12"><circle cx="6" cy="6" r="6" fill="var(--wine)"/><path d="M3 6.2l2 2 4-4.4" stroke="#fff" stroke-width="1.6" fill="none"/></svg>Fussreflexzonenmassage</li>
    </ul>
  </div>

  <div class="photo" role="img" aria-label="Foto: Schultermassage" style="left:900px;top:390px;width:180px;height:180px;background:radial-gradient(circle at 45% 50%,#f0c9ad,#b8826a)"></div>
  <div class="photo" role="img" aria-label="Foto: Rückenmassage mit beiden Händen" style="left:720px;top:500px;width:280px;height:280px;background:radial-gradient(circle at 45% 45%,#f6d8c2,#d8a283 60%,#f3ede8)"></div>
  <div class="badge" style="left:780px;top:420px;width:118px;height:118px;font-size:12px">individuelle<br>Behandlungen mit<br>Alternativmedizin</div>
</section>

<section class="spread spread--outside" aria-label="Aussenseiten">
  <svg class="shapes" viewBox="0 0 1120 792" aria-hidden="true">
    <rect x="373" y="0" width="374" height="792" fill="var(--wine)"/>
    <path d="M747 160Q900 205 1120 130V0H747Z" fill="#f3d9c6"/>
    <path d="M747 168Q910 215 1120 140" fill="none" stroke="var(--wine)" stroke-width="7"/>
    <path d="M747 770Q940 740 1120 640V792H747Z" fill="var(--wine)"/>
  </svg>

  <div class="photo photo--rect" role="img" aria-label="Foto: entspannte Frau auf der Massageliege" style="left:747px;top:0;width:373px;height:150px;background:linear-gradient(90deg,#f1cfb6,#f7ece2);clip-path:ellipse(110% 100% at 60% 0)"></div>

  <div class="block" style="left:34px;top:48px;width:320px">
    <h2 class="heading">Persönlich</h2>
    <p class="personal-quote">„Ich freue mich wenn ich Sie unterstützen darf zur Verbesserung Ihrer Gesundheit. Persönlich – Individuell – Professionell“</p>
    <h2 class="heading" style="margin-top:24px">Aus- &amp; Fortbildungen</h2>
    <ul class="ticks" style="margin-top:10px">
      <li style="text-transform:none"><svg width="11" height="11" viewBox="0 0 12 12"><circle cx="6" cy="6" r="6" fill="var(--wine)"/><path d="M3 6.2l2 2 4-4.4" stroke="#fff" stroke-width="1.6" fill="none"/></svg>Trad. Europäische Naturheilpraktikerin, TEN</li>
      <li style="text-transform:none"><svg width="11" height="11" viewBox="0 0 12 12"><circle cx="6" cy="6" r="6" fill="var(--wine)"/><path d="M3 6.2l2 2 4-4.4" stroke="#fff" stroke-width="1.6" fill="none"/></svg>Akupunktur, TCM</li>
      <li style="text-transform:none"><svg width="11" height="11" viewBox="0 0 12 12"><circle cx="6" cy="6" r="6" fill="var(--wine)"/><path d="M3 6.2l2 2 4-4.4" stroke="#fff" stroke-width="1.6" fill="none"/></svg>Chinesische Kräuter, TCM</li>
      <li style="text-transform:none"><svg width="11" height="11" viewBox="0 0 12 12"><circle cx="6" cy="6" r="6" fill="var(--wine)"/><path d="M3 6.2l2 2 4-4.4" stroke="#fff" stroke-width="1.6" fill="none"/></svg>Craniosacral Therapie</li>
      <li style="text-transform:none"><svg width="11" height="11" viewBox="0 0 12 12"><circle cx="6" cy="6" r="6" fill="var(--wine)"/><path d="M3 6.2l2 2 4-4.4" stroke="#fff" stroke-width="1.6" fill="none"/></svg>Funktionelle Orthonomie und Integration, FOI</li>
    </ul>
    <p class="strong-note" style="margin-top:14px">Mehr als 13 Jahre Erfahrung im therapeutischen Bereich in eigener Praxis, bei Norvantis Office Zürich und diverse Praktika.</p>
  </div>

  <div class="photo photo--rect" role="img" aria-label="Foto: Hände setzen Akupunkturnadeln" style="left:0;top:560px;width:373px;height:232px;background:linear-gradient(135deg,#5f93c4,#f2c8aa 55%,#e9b08f);clip-path:ellipse(120% 100% at 50% 100%)"></div>
  <div class="badge" style="left:40px;top:600px;width:120px;height:120px;font-size:13px">jetzt Termin<br>vereinbaren<br>078 412 36 85</div>

  <div class="block panel-dark" style="left:410px;top:40px;width:300px">
    <h2 class="heading">Anfahrt</h2>
  </div>
  <div class="map" role="img" aria-label="Kartenausschnitt mit Lage der Praxis" style="left:410px;top:100px;width:300px;height:240px"></div>

  <div class="block panel-dark" style="left:410px;top:420px;width:310px">
    <h2 class="heading">Kontakt</h2>
    <p style="font-family:'Montserrat',sans-serif;font-weight:600;font-size:13px;margin:18px 0 10px;letter-spacing:.4px">AKUPUNKTUR TCM • MASSAGEN</p>
    <p class="contact-line"><svg width="12" height="14" viewBox="0 0 12 14"><path d="M6 13S1 8 1 5a5 5 0 0 1 10 0c0 3-5 8-5 8z" fill="none" stroke="#fff" stroke-width="1.3"/><circle cx="6" cy="5" r="1.7" fill="#fff"/></svg>Birkenweg 14 | 3280 Murten</p>
    <p class="contact-line"><svg width="12" height="12" viewBox="0 0 12 12"><path d="M2 1l2.5 0 1 3-1.5 1a7 7 0 0 0 3 3l1-1.5 3 1V11A9 9 0 0 1 1 2z" fill="none" stroke="#fff" stroke-width="1.2"/></svg>Tel. +41 (0)78 412 36 85</p>
    <p style="margin-top:60px;text-align:center"><span class="web">WWW.PRAXIS-LINDHOF.CH</span></p>
  </div>

  <div class="photo photo--rect" role="img" aria-label="Porträtfoto der Therapeutin" style="left:765px;top:200px;width:160px;height:480px;background:linear-gradient(180deg,#f3ede2,#d9c6b0 35%,#2c3540 60%,#6d84a8)"></div>

  <div class="dot" style="left:940px;top:210px;width:32px;height:32px"></div>
  <p class="service" style="left:980px;top:212px">Chinesische<br>Medizin (TCM)</p>
  <div class="dot" style="left:940px;top:335px;width:32px;height:32px"></div>
  <p class="service" style="left:980px;top:337px">Craniosacrale<br>Therapie</p>
  <div class="dot" style="left:940px;top:460px;width:32px;height:32px"></div>
  <p class="service" style="left:980px;top:462px">Funktionelle Orthonomie<br>&amp; Integration (FOI)</p>

  <div class="brand" style="top:580px"><span class="brand-mark"></span>PraxisLindhof</div>
  <p class="brand-sub" style="top:612px">KomplementärPraxisLindhof</p>
</section>

</body>
</html>
```